Luxury Japanese Matcha Green Tea Packaging Full Packet Design

We're looking for a quality full pack design (front and back) for Ceremonial Grade and Premium Grade Matcha to sell on Bazarly. We need a 2D versions of front and back images in photoshop and JPG. We also need a 3D versions of front and back for marketing purposes.

You can see our current styling and pack at www.leafwrights.co.uk. However, we want to improve the design and go more professional, simple and elegant with the brand. The last design was from 3 years a go. But hopefully you can see what we are about.

The design will be identical both both packs:

Pack 1: 230mm x 140mm - Premium Grade
Pack 2: 170mm x 120mm - Ceremonial Grade

The design needs to fit both sizes, with pack 1 saying Premium Grade and pack 2 saying Ceremonial Grade.

As many colours as needed, printing is CMYK + White digital printed.

Front of pack:

Product Headline:

Organic Handpicked
Stoneground Japanese Matcha
Green Tea Powder

抹茶

Text: Premium Grade (pack 1) / Ceremonial Grade (pack 2)

100g (pack 1) / 40g (pack 2)

(EU Organic logo)

Back of pack:

Organic Certified GB-ORG-17
Stone Ground Ceremonial Grade Matcha from Uji

Ingredients: 100% Organic Matcha Green Tea Powder

Place of origin: Japan, Store in a cool, dry, dark place
Keep sealed at all times, Best Before 31/03/2020
Not recommended for use if pregnant or nursing

Your next order is ready for you at www.VerdeHour.co.uk

Preparing Traditional Matcha Tea:
Sift 1-2g or 1/2 teaspoon of Matcha Green Tea
powder into a bowl or large cup. Add 1/2 cup of hot water
at drinking temperature. Whisk with Bamboo or
Electric Whisk until frothy. Drink immediately.

Preparing Matcha Latte:
Sift 1-2g of Matcha Power into a cup, mix in 2-3 tablespoons of hot water.
Add hot milk and sweetener if desired. Whisk thoroughly.

Nutritional Information:

Per 1g Per 100g
Energy 14.44kJ 1446kJ
3.44kCal 345kCal
Fat 0.04g 4g
Saturates <0.01g 0.6g
Carbohydrates 0.76g 76g
of which sugars 0.47g 47.2g
Protein 0.144g 14.5g
Salt <0.01g 126mg

Per 1g Per 100g
Calcium 1.88mg 191mg
Potassium 94.8mg 3750mg
Iron <0.1g 1.6mg
Zinc <0.1g 1.72mg
Vitamin A 120µg (15% RDA) 2400µg (150% RDA)
Vitamin C 3mg (4% RDA) 60mg (75% RDA)
Folic acid 6µg (6% RDA) 60µg (30% RDA)
Riboflavin 0.1mg (4% RDA) 1.4mg (96% RDA)
Caffeine 17mg 1700mg

Calvert Reach Ltd. T/A Leafwrights
Company Number: 07415926
Registered Office: 9 The Yard, Hartwell Rd
Newbury, Berkshire, RG17 2PN
social@leafwrights.co.uk
Local Call +44 (0) 20 7946 0531 / Freephone +44 (0) 800 914 0627

This supplement should not be used as a substitute for a varied diet Do not exceed the recommended daily dose.

For more information on Matcha, download the free eBook at www.VerdeLeafGuide.com

Please consult a healthcare practitioner if you are pregnant or taking prescription medicine before using this product.

Recommended daily dose

1-5g daily

Storage information: Store in a cool dry place away from sunlight, moisture, and heat. Keep contents dry.

Logos for back of pack:
EU Organic logo with 'GB-ORG-17 Non-EU Agriculture' written directly underneath it.
Vegan logo
Natural Produce Alliance logo
Bazarly Barcode

Additional deisgn notes:

We have included a design that we like.

The top 2cm will be torn off by the user, so should not contain any key information.

Target Market(s)

High End health and wellness Consumers

Colors
acd036
0455a3
edf8f6

Requirements
Must have
• Stand out on Bazarly. Show the product to be premium.

```html
<!DOCTYPE html>
<html lang="en">
<head>
<meta charset="utf-8">
<title>Leafwrights Premium Grade Matcha – Front of Pack</title>
<link rel="stylesheet" href="https://fonts.googleapis.com/css2?family=Didact+Gothic&family=Jost:wght@400;500&family=Noto+Sans+JP:wght@300&display=swap">
<style>
  :root {
    --backdrop: #e9e9e9;
    --pouch: #0e0f0f;
    --pouch-edge: #1b1c1c;
    --leaf-green: #6cbf3a;
    --tag-green: #4ea53a;
    --text-white: #f4f4f4;
    --matcha-deep: #4d6a1c;
    --matcha-light: #8aa83a;
    --bowl: #221816;
  }
  * { box-sizing: border-box; margin: 0; padding: 0; }
  html, body { width: 1200px; height: 1182px; overflow: hidden; }
  body { background: var(--backdrop); position: relative; }

  .pouch {
    position: absolute; left: 348px; top: 149px;
    width: 504px; height: 884px;
    background: var(--pouch);
    border-radius: 10px 10px 6px 6px;
    overflow: hidden;
    text-align: center;
    color: var(--text-white);
  }
  .tear-strip {
    position: absolute; left: 0; right: 0; top: 0; height: 92px;
    border-bottom: 2px solid var(--pouch-edge);
  }
  .zip-line {
    position: absolute; left: 0; right: 0; top: 104px; height: 3px;
    background: var(--pouch-edge);
  }
  .brand {
    position: absolute; left: 0; right: 0; top: 176px;
    display: flex; justify-content: center; align-items: center; gap: 10px;
  }
  .brand-dot { width: 14px; height: 14px; border-radius: 50%; background: var(--leaf-green); }
  .brand-name {
    font-family: "Didact Gothic", sans-serif; font-size: 40px;
    color: var(--leaf-green); letter-spacing: 0.5px; line-height: 1;
  }
  .kicker {
    position: absolute; left: 0; right: 0; top: 245px;
    font-family: "Jost", sans-serif; font-size: 16px; letter-spacing: 0.2px;
  }
  .headline {
    position: absolute; left: 0; right: 0; top: 266px;
    font-family: "Jost", sans-serif; font-weight: 500; line-height: 1;
  }
  .headline-main { display: block; font-size: 38px; letter-spacing: -0.5px; }
  .headline-sub { display: block; font-size: 30px; margin-top: 6px; font-weight: 400; letter-spacing: -0.3px; }
  .product-tag {
    position: absolute; left: 50%; top: 348px; transform: translateX(-50%);
    background: var(--tag-green); padding: 2px 9px;
    font-family: "Jost", sans-serif; font-size: 16px; white-space: nowrap;
  }
  .kanji {
    position: absolute; left: 0; right: 0; top: 380px;
    font-family: "Noto Sans JP", sans-serif; font-weight: 300; font-size: 56px;
    letter-spacing: 14px; line-height: 1;
  }
  .organic-badge { position: absolute; left: 212px; top: 462px; }
  .photo-area {
    position: absolute; left: 0; right: 0; top: 586px; bottom: 0;
    background:
      radial-gradient(ellipse 42% 40% at 50% 52%, var(--matcha-light) 0%, var(--matcha-deep) 60%, transparent 62%),
      radial-gradient(ellipse 60% 55% at 50% 55%, var(--bowl) 0%, #120c0b 70%, #3a2a1e 100%);
  }
  .grade {
    position: absolute; left: 120px; top: 560px;
    font-family: "Jost", sans-serif; font-size: 39px; color: var(--leaf-green);
    transform: rotate(-7deg); transform-origin: left bottom; white-space: nowrap;
    letter-spacing: 0.5px;
  }
  .weight {
    position: absolute; left: 0; right: 0; top: 826px;
    font-family: "Jost", sans-serif; font-size: 29px;
  }
</style>
</head>
<body>
  <main class="pouch">
    <div class="tear-strip"></div>
    <div class="zip-line"></div>

    <div class="brand">
      <span class="brand-dot"></span>
      <span class="brand-name">Leafwrights</span>
    </div>

    <p class="kicker">ORGANIC HANDPICKED</p>
    <h1 class="headline">
      <span class="headline-main">STONEGROUND</span>
      <span class="headline-sub">JAPANESE MATCHA</span>
    </h1>
    <p class="product-tag">GREEN TEA POWDER</p>
    <p class="kanji" lang="ja">抹茶</p>

    <svg class="organic-badge" width="80" height="50" viewBox="0 0 80 50" role="img" aria-label="Organic certification badge">
      <ellipse cx="40" cy="25" rx="38" ry="14" transform="rotate(-28 40 25)" fill="none" stroke="#6cbf3a" stroke-width="2"/>
    </svg>

    <div class="photo-area" role="img" aria-label="Photograph of matcha powder heaped in a dark bowl on burlap"></div>

    <p class="grade">PREMIUM GRADE</p>
    <p class="weight">100g</p>
  </main>
</body>
</html>
```